Poetry Book Cover Design Project

Looking for a minimalistic book cover design for a collection of poems. The book title is "Before The Morning Turns To Glass". There are three parts to the book. First covers poetry in the theme of Rage. Second love and desire. The third is strange poems. Essentially the sections are "Rage", "Desire" and the "Strange". The reason for the title "Before The Morning Turns To Glass" is as if someone is writing these till life changes towards the intended outcome as felt in each poem. I want to have the author's name "Nirosha Kulathunge" at the bottom. Ilustration attached.
- Minimalistic

```html
<!DOCTYPE html>
<html lang="en">
<head>
<meta charset="utf-8">
<title>Before The Morning Turns To Glass — Nirosha Kulathunge</title>
<link rel="stylesheet" href="https://fonts.googleapis.com/css2?family=EB+Garamond:wght@400;500&family=Montserrat:wght@500&display=swap">
<style>
  :root {
    --backdrop: #c9cecf;
    --cover-blue: #12457a;
    --band-blue: #17396a;
    --title-white: #ffffff;
    --accent-red: #e0242b;
  }
  html, body {
    margin: 0;
    padding: 0;
    width: 1072px;
    height: 1200px;
    overflow: hidden;
    background: var(--backdrop);
  }
  .book-cover {
    position: absolute;
    left: 186px;
    top: 40px;
    width: 700px;
    height: 1120px;
    background: var(--cover-blue);
    overflow: hidden;
  }
  .book-title {
    position: absolute;
    right: 78px;
    top: 236px;
    margin: 0;
    font-family: "EB Garamond", Georgia, serif;
    font-weight: 400;
    font-size: 92px;
    line-height: 0.8;
    letter-spacing: -0.045em;
    color: var(--title-white);
    text-align: right;
  }
  .book-title span { display: block; }
  .eye-mark {
    position: absolute;
    left: 103px;
    top: 598px;
    width: 189px;
    height: 80px;
  }
  .vertical-band {
    position: absolute;
    left: 110px;
    top: 634px;
    width: 177px;
    height: 486px;
    background: var(--band-blue);
  }
  .author-line {
    position: absolute;
    left: 362px;
    top: 1040px;
    display: flex;
    align-items: center;
    gap: 10px;
  }
  .author-name {
    font-family: "Montserrat", Arial, sans-serif;
    font-weight: 500;
    font-size: 17px;
    letter-spacing: 0.04em;
    text-transform: uppercase;
    color: var(--title-white);
    white-space: nowrap;
  }
  .imprint-square {
    width: 14px;
    height: 14px;
    background: var(--title-white);
  }
</style>
</head>
<body>
  <main class="book-cover">
    <div class="vertical-band"></div>
    <svg class="eye-mark" viewBox="0 0 189 80" role="img" aria-label="Small red line drawing of a closed eye with lashes">
      <rect x="0" y="20" width="189" height="40" rx="20" fill="var(--accent-red)"/>
    </svg>
    <h1 class="book-title">
      <span>Before</span>
      <span>The</span>
      <span>Morning</span>
      <span>Turns</span>
      <span>To</span>
      <span>Glass</span>
    </h1>
    <div class="author-line">
      <span class="author-name">Nirosha Kulathunge</span>
      <span class="imprint-square"></span>
    </div>
  </main>
</body>
</html>
```